ORVI LTH website - sleek, sophisticated, uplifting

ORVI Institute for Restorative Care is a cutting-edge medical clinic aimed at providing treatment for various chronic conditions and help people stave off the declines usually associated with aging. We utilize the latest technology in regenerative medicine to help people with autoimmune conditions, musculoskeletal problems and chronic pain, neurodegenerative conditions, male enhancement, facial rejuvenation and hair restoration, etc. We provide personalized medicine, through highly compassionate and competent doctors and staff.

please look at my current website which is not focused on regenerative medicine, but some contents can stay, as far as the philosophy of the treatment: www.pbmosaicwellness-example.com. But the reason I am changing the name of the clinic is because the focus of the medical practice is shifted entirely to "regenerative medicine" - using the body's own healing mechanism such as stem cells and growth factors...

Please DO NOT recycle old graphics and pictures. I want this site to be brand new, fresh and original.

Would like the website to be more sophisticated and nicer-looking than this website: www.duskmere-example.com

Target Market(s)

People who care a great deal about their health (above age 35), wants to prevent declines in their looks and health as they are getting older. Generally high income sector of the society that can afford self-pay (no insurance accepted) expensive stem cell treatment ranging from $4000 to $20,000.

Industry/Entity Type

Healthcare

Coding

Coded - Design and coding required

Number of Pages Required

5+ page

Font styles to use
Sans Serif
Other font styles liked:
• Al Bayan, Avenir, Didot, Open Sans or Tsukushi A Round Gothic for central text, but may use Chalkboard for titles, or others as seen fit

Colors

Designer to choose colors to be used in the design.

Requirements
Must have
• Ultra modern look, very clean & sleek images and layout, portraying a sense of sophistication and confidence. Works beautifully well with existing logo. Give a sense that the clinic employs cutting-edge science, and provide highly competent & compassionate services.
• More sophisticated and nicer-looking than this website: www.duskmere-example.com
Nice to have
• many pages and links to science articles
Should not have
• fonts too playful or hard to read.

```html
<!DOCTYPE html>
<html lang="en">
<head>
<meta charset="utf-8">
<title>ORVI LTH — Website Screens</title>
<link href="https://fonts.googleapis.com/css2?family=Advent+Pro:wght@300;400&display=swap" rel="stylesheet">
<style>
:root{
  --ink:#1d1d1d;
  --muted:#6f6f6f;
  --paper:#ffffff;
  --bar:#f6f6f7;
  --rule:#e4e4e6;
  --gold:#e0a92a;
  --shade:#8d8d8d;
  --shade-ink:#262626;
}
*{margin:0;padding:0;box-sizing:border-box}
html,body{width:1200px;height:1200px;overflow:hidden;background:var(--paper)}
body{position:relative;font-family:"Advent Pro",sans-serif;color:var(--ink)}
.screen{position:absolute;overflow:hidden;background:var(--paper)}
.screen svg.art{position:absolute;left:0;display:block}
.navbar{position:absolute;left:0;right:0;top:0;height:32px;background:var(--bar);display:flex;align-items:center;padding-left:6px}
.brand{display:flex;align-items:center;gap:3px;font-weight:400;color:var(--ink)}
.brand-mark{width:7px;height:7px;background:var(--gold)}
.navbar .brand{font-size:11px;width:51px}
.nav-links{display:flex;gap:12px;font-size:7px;font-weight:400}
.col-title{position:absolute;font-weight:300;line-height:1}
.body-copy{position:absolute;font-weight:400;text-align:justify;text-align-last:left}
.desk .col-title{font-size:19px}
.desk .body-copy{font-size:6.4px;line-height:11.5px;width:240px}
.mobile-head{position:absolute;left:0;right:0;top:0;background:var(--bar)}
.burger{position:absolute;display:flex;flex-direction:column;justify-content:space-between}
.burger span{display:block;height:2px;background:var(--ink)}
/* screens */
.about-desk{left:0;top:0;width:600px;height:336px}
.services-desk{left:600px;top:0;width:600px;height:340px}
.services-desk-lower{left:598px;top:340px;width:602px;height:338px}
.service-mobile{left:51px;top:336px;width:493px;height:864px;border-right:1px solid var(--rule)}
.menu-mobile{left:600px;top:678px;width:296px;height:522px}
.about-mobile{left:896px;top:678px;width:296px;height:522px}
.service-mobile .col-title{left:25px;top:650px;font-size:48px}
.service-mobile .body-copy{left:25px;top:706px;width:443px;font-size:19.5px;line-height:29.5px;font-weight:300}
.phone .col-title{left:14px;top:314px;font-size:30px}
.phone .body-copy{left:14px;top:350px;width:268px;font-size:13px;line-height:18px;font-weight:300}
.menu-list{position:absolute;left:14px;right:14px;top:16px;list-style:none}
.menu-list li{height:48px;display:flex;align-items:center;justify-content:center;font-size:12px;border-bottom:1px solid var(--rule)}
.menu-list li:last-child{border-bottom:none}
.menu-mobile .dim{position:absolute;left:0;right:0;top:274px;bottom:0;background:var(--shade)}
.menu-mobile .col-title,.menu-mobile .body-copy{color:var(--shade-ink)}
</style>
</head>
<body>

<!-- Desktop: About page -->
<section class="screen desk about-desk">
  <svg class="art" style="top:0" width="600" height="200" viewBox="0 0 600 200">
    <defs>
      <linearGradient id="dnaBlue" x1="0" y1="0" x2="1" y2="0">
        <stop offset="0" stop-color="#1c3f8c"/><stop offset=".45" stop-color="#3f7fd0"/><stop offset=".75" stop-color="#2157b8"/><stop offset="1" stop-color="#8fb2d6"/>
      </linearGradient>
    </defs>
    <polygon role="img" aria-label="Hero image: blue digital brain and DNA helix" points="0,32 600,28 600,174 425,191 0,174" fill="url(#dnaBlue)"/>
  </svg>
  <nav class="navbar"><div class="brand"><span class="brand-mark"></span>ORVI</div>
    <div class="nav-links"><span>Home</span><span>About us</span><span>Services</span><span>Contact</span></div></nav>
  <h2 class="col-title" style="left:30px;top:224px">About 1</h2>
  <p class="body-copy" style="left:30px;top:246px">One Lorem Ipsum is simply dummy text of the printing and typesetting industry. Lorem Ipsum has been the industry's standard dummy text ever since the 1500s, when an unknown printer took a galley of type and scrambled it to make a type specimen book. It has survived not only five centuries, but also the leap into electronic typesetting, remaining essentially unchanged. It was popularised in the 1960s with the release of Typemark sheets containing Lorem Ipsum passages, and more recently with desktop publishing software like Quillset Layout including versions of Lorem Ipsum.</p>
  <h2 class="col-title" style="left:330px;top:224px">About 2</h2>
  <p class="body-copy" style="left:330px;top:246px">Two Lorem Ipsum is simply dummy text of the printing and typesetting industry. Lorem Ipsum has been the industry's standard dummy text ever since the 1500s, when an unknown printer took a galley of type and scrambled it to make a type specimen book. It has survived not only five centuries, but also the leap into electronic typesetting, remaining essentially unchanged. It was popularised in the 1960s with the release of Typemark sheets containing Lorem Ipsum passages, and more recently with desktop publishing software like Quillset Layout including versions of Lorem Ipsum.</p>
</section>

<!-- Desktop: Services page, top -->
<section class="screen desk services-desk">
  <svg class="art" style="top:0" width="600" height="260" viewBox="0 0 600 260">
    <defs>
      <linearGradient id="sunset" x1="0" y1="0" x2="0" y2="1">
        <stop offset="0" stop-color="#e9c7ae"/><stop offset=".45" stop-color="#f0c2a6"/><stop offset=".75" stop-color="#d9b3a6"/><stop offset="1" stop-color="#c9b8b4"/>
      </linearGradient>
    </defs>
    <polygon role="img" aria-label="Hero image: woman with raised arms facing a sunset sky" points="0,28 300,38 600,28 600,225 280,250 0,226" fill="url(#sunset)"/>
  </svg>
  <nav class="navbar"><div class="brand"><span class="brand-mark"></span>ORVI</div>
    <div class="nav-links"><span>Home</span><span>About us</span><span>Services</span><span>Contact</span></div></nav>
  <h2 class="col-title" style="left:30px;top:282px">Service 1</h2>
  <p class="body-copy" style="left:30px;top:305px">One Lorem Ipsum is simply dummy text of the printing and typesetting industry. Lorem Ipsum has been the industry's standard dummy text ever since the 1500s, when an unknown printer took a galley of type and scrambled it to make a type specimen book.</p>
  <h2 class="col-title" style="left:331px;top:282px">Service 2</h2>
  <p class="body-copy" style="left:331px;top:305px">Two Lorem Ipsum is simply dummy text of the printing and typesetting industry. Lorem Ipsum has been the industry's standard dummy text ever since the 1500s, when an unknown printer took a galley of type and scrambled it to make a type specimen book.</p>
</section>

<!-- Desktop: Services page, lower -->
<section class="screen desk services-desk-lower">
  <svg class="art" style="top:0" width="602" height="338" viewBox="0 0 602 338">
    <polygon role="img" aria-label="Image band: woman with raised arms at sunset" points="0,224 178,194 602,214 602,338 0,338" fill="url(#sunset)"/>
  </svg>
  <nav class="navbar"><div class="brand"><span class="brand-mark"></span>ORVI</div>
    <div class="nav-links"><span>Home</span><span>About us</span><span>Services</span><span>Contact</span></div></nav>
  <h2 class="col-title" style="left:30px;top:50px">Service 1</h2>
  <p class="body-copy" style="left:30px;top:73px">One Lorem Ipsum is simply dummy text of the printing and typesetting industry. Lorem Ipsum has been the industry's standard dummy text ever since the 1500s, when an unknown printer took a galley of type and scrambled it to make a type specimen book. It has survived not only five centuries, but also the leap into electronic typesetting, remaining essentially unchanged. It was popularised in the 1960s with the release of Typemark sheets containing Lorem Ipsum passages, and more recently with desktop publishing software like Quillset Layout including versions of Lorem Ipsum.</p>
  <h2 class="col-title" style="left:331px;top:50px">Service 2</h2>
  <p class="body-copy" style="left:331px;top:73px">Two Lorem Ipsum is simply dummy text of the printing and typesetting industry. Lorem Ipsum has been the industry's standard dummy text ever since the 1500s, when an unknown printer took a galley of type and scrambled it to make a type specimen book. It has survived not only five centuries, but also the leap into electronic typesetting, remaining essentially unchanged. It was popularised in the 1960s with the release of Typemark sheets containing Lorem Ipsum passages, and more recently with desktop publishing software like Quillset Layout including versions of Lorem Ipsum.</p>
</section>

<!-- Mobile: Service 1 -->
<section class="screen service-mobile">
  <svg class="art" style="top:0" width="493" height="640" viewBox="0 0 493 640">
    <polygon role="img" aria-label="Photo: woman with raised arms facing the sea at sunset" points="0,92 493,76 493,532 333,616 0,532" fill="url(#sunset)"/>
  </svg>
  <header class="mobile-head" style="height:82px;clip-path:polygon(0 0,100% 0,100% 100%,0 100%)">
    <div class="brand" style="position:absolute;left:16px;top:34px;font-size:22px;gap:6px"><span class="brand-mark" style="width:12px;height:12px"></span>ORVI</div>
    <div class="burger" style="left:426px;top:25px;width:39px;height:32px"><span></span><span></span><span></span></div>
  </header>
  <h1 class="col-title">Service 1</h1>
  <p class="body-copy">One: Lorem Ipsum is simply dummy text of the printing and typesetting industry. Lorem Ipsum has been the industry's standard dummy text ever since the 1500s, when an unknown printer took a galley of type and scrambled it to make a type specimen book. It has survived not only five centuries</p>
</section>

<!-- Mobile: open menu -->
<section class="screen phone menu-mobile">
  <svg class="art" style="top:0" width="296" height="300" viewBox="0 0 296 300">
    <polygon role="img" aria-label="Image band: blue DNA helix" points="0,222 296,208 296,300 0,300" fill="url(#dnaBlue)"/>
  </svg>
  <div class="brand" style="position:absolute;left:8px;top:22px;font-size:12px"><span class="brand-mark"></span>ORVI</div>
  <div class="burger" style="left:257px;top:14px;width:19px;height:19px"><span style="height:1.5px"></span><span style="height:1.5px"></span><span style="height:1.5px"></span></div>
  <ul class="menu-list"><li>Home</li><li>About us</li><li>Services</li><li>Contact</li></ul>
  <svg class="art" style="top:0" width="296" height="300" viewBox="0 0 296 300"><polygon points="0,260 296,250 296,300 0,300" fill="#8d8d8d" opacity=".85"/><polygon points="0,218 200,262 296,230 296,210 0,210" fill="#ffffff"/></svg>
  <div class="dim"></div>
  <h2 class="col-title">About 1</h2>
  <p class="body-copy">One: Lorem Ipsum is simply dummy text of the printing and typesetting industry. Lorem Ipsum has been the industry's standard dummy text ever since the 1500s, when an unknown printer took a galley of type and scrambled it to make a type specimen book. It has survived not only five centuries, but also the leap into electronic typesetting, remaining essentially unchanged. It was popularised in the 1960s with the release of Typemark sheets containing Lorem Ipsum passages, and more recently with desktop publishing software like Quillset Layout</p>
</section>

<!-- Mobile: About -->
<section class="screen phone about-mobile">
  <svg class="art" style="top:0" width="296" height="300" viewBox="0 0 296 300">
    <polygon role="img" aria-label="Photo: blue digital head and DNA helix" points="0,54 296,42 296,274 152,296 0,274" fill="url(#dnaBlue)"/>
  </svg>
  <header class="mobile-head" style="height:44px;clip-path:polygon(0 0,100% 0,100% 95%,0 100%)">
    <div class="brand" style="position:absolute;left:8px;top:22px;font-size:12px"><span class="brand-mark"></span>ORVI</div>
    <div class="burger" style="left:255px;top:14px;width:19px;height:19px"><span style="height:1.5px"></span><span style="height:1.5px"></span><span style="height:1.5px"></span></div>
  </header>
  <h2 class="col-title">About 1</h2>
  <p class="body-copy">One: Lorem Ipsum is simply dummy text of the printing and typesetting industry. Lorem Ipsum has been the industry's standard dummy text ever since the 1500s, when an unknown printer took a galley of type and scrambled it to make a type specimen book. It has survived not only five centuries, but also the leap into electronic typesetting, remaining essentially unchanged. It was popularised in the 1960s with the release of Typemark sheets containing Lorem Ipsum passages, and more recently with desktop publishing software like Quillset Layout</p>
</section>

</body>
</html>
```